Book Title: “Ember: Road of Quiet Dawn” Please see the attachment “Text on the cover”.

Book Cover Design Instructions: This book is meant for people of all religions and nationalities. Therefore, on the cover, there should be no mosque or an object specific to any religion. The primary emphasis should be on the "unconditional love of God." Therefore, use universal symbols of love. The second priority themes could be Sufism, Peace, and self-improvement. Rest is your imagination. Please also see the attachment: 'Book description and author's Bio.'
This book has the potential to be a best seller. Please do a good job.
What Book Cover Formats are required: A designer should submit cover designs in three formats: (1) eBook, (2) Paperback, and (3) Hardback. These books will be published on Velmora PBX.
Format requirements for eBooks are available from: https://pbx.velmora-press.example/en_US/help/topic/R731928405.
You can find paperback and hardback cover measurements from: https://pbx.velmora-press.example/en_US/cover-calculator
• To complete the project, all three formats should be accepted by Velmora PBX.
• The book interior trim size is 6.14 X 9.21 inches.
• Interior Type: Premium color.
• No bleed.
• I do not upload barcode. So, the back cover should have room for Velmora to print the barcode.
• Number of pages 126.
Compensation for the designer: After selecting one designer, I will increase the amount by $200 on Artlumo to compensate for three deliverables.
Follow-up of the Project:
After the book is published, I may need minor revisions. For example, the number of pages may change. Therefore, I will need the same design in revised sizes. In that case, I will pay $25 for each revision. For example, if the number of pages changes, I will need a different spine for paperback and hardback, then I will pay the artist $25 + $25 = $50 for both designs.
List of Enclosers:
1. Text on the cover.
2. Book description and author's Bio for the back cover.
3. Later, I will upload my picture for the book's back cover.

Target Market(s)

Any adult

Industry/Entity Type

Any industry

Requirements
Must have
• Three Deliverables

```html
<!DOCTYPE html>
<html lang="en">
<head>
<meta charset="utf-8">
<title>Ember: Road of Quiet Dawn — Cover Wrap</title>
<link rel="stylesheet" href="https://fonts.googleapis.com/css2?family=Playfair+Display:ital,wght@0,500;0,600;0,700;1,400&family=Poppins:wght@400;500;600&display=swap">
<style>
  :root{
    --page:#ffffff;
    --ink:#1f1a14;
    --ink-soft:#2b2620;
    --ember-1:#f08a2a;
    --ember-2:#d4531a;
    --sky-top:#7f9fb2;
    --sky-mid:#d9e0df;
    --haze:#eed6c6;
    --peach:#f3c8ad;
    --sea:#b8c3c6;
    --sun:#fbe2a8;
    --art-top:#ead8bf;
    --art-mid:#d9a877;
    --art-low:#9fae8e;
    --art-base:#d9a3a6;
    --blank:#ffffff;
  }
  *{margin:0;padding:0;box-sizing:border-box}
  html,body{width:1200px;height:1200px;overflow:hidden;background:var(--page)}
  .canvas{position:relative;width:1200px;height:1200px}
  .wrap{
    position:absolute;left:27px;top:178px;width:1147px;height:845px;overflow:hidden;
    box-shadow:0 3px 8px rgba(0,0,0,.25);
    background:
      radial-gradient(ellipse 260px 200px at 1080px 640px, var(--sun) 0%, rgba(251,226,168,0) 100%),
      linear-gradient(180deg,var(--sky-top) 0%,var(--sky-mid) 38%,var(--haze) 62%,var(--peach) 78%,var(--sea) 100%);
  }
  .front-artwork{
    position:absolute;left:640px;top:390px;width:507px;height:455px;
    background:linear-gradient(180deg,var(--art-top) 0%,var(--art-mid) 55%,var(--art-low) 85%,var(--art-base) 100%);
  }
  .accent{color:var(--ember-2)}
  .back-title{
    position:absolute;left:31px;top:24px;
    font:500 38px/1.2 "Playfair Display",serif;color:var(--ink);letter-spacing:.5px;white-space:nowrap;
  }
  .back-subtitle{
    position:absolute;left:33px;top:71px;
    font:600 15.6px/1.2 "Poppins",sans-serif;color:var(--ink);white-space:nowrap;letter-spacing:-.1px;
  }
  .blurb{
    position:absolute;left:25px;top:113px;width:512px;
    font:500 11.5px/15px "Poppins",sans-serif;color:var(--ink);letter-spacing:-.2px;
  }
  .blurb p{margin-bottom:15px}
  .blurb em{font-family:"Playfair Display",serif;font-style:italic}
  .questions{list-style:none;margin:12px 0 14px 0}
  .questions li{
    position:relative;padding-left:20px;margin-bottom:15px;
    font:italic 400 12px/15px "Playfair Display",serif;letter-spacing:0;
  }
  .questions li span{position:absolute;left:0;font-size:10px}
  .author-photo{position:absolute;left:35px;top:580px;width:91px;height:102px;border:1px solid var(--ink)}
  .author-name-back{position:absolute;left:137px;top:594px;font:500 18.5px/1 "Playfair Display",serif;color:var(--ink);letter-spacing:.4px}
  .author-bio{position:absolute;left:139px;top:625px;width:400px;font:400 11px/15px "Poppins",sans-serif;color:var(--ink)}
  .barcode-room{position:absolute;left:359px;top:705px;width:180px;height:107px;background:var(--blank)}
  .spine{position:absolute;left:539px;top:0;width:50px;height:845px}
  .spine-text{
    position:absolute;left:50%;transform-origin:0 0;transform:rotate(90deg);white-space:nowrap;
    font:500 18px/1 "Playfair Display",serif;color:var(--ink);margin-left:20px;
  }
  .spine-title{top:100px}
  .spine-author{top:576px;font-weight:600}
  .front{position:absolute;left:589px;top:0;width:558px;height:845px;text-align:center}
  .front-kicker{
    position:absolute;left:0;right:0;top:18px;
    font:600 120px/1 "Playfair Display",serif;letter-spacing:2px;
    background:linear-gradient(180deg,var(--ember-1),var(--ember-2));-webkit-background-clip:text;background-clip:text;color:transparent;
    filter:drop-shadow(1px 2px 2px rgba(80,30,0,.35));
  }
  .front-title{
    position:absolute;left:0;right:0;top:134px;
    font:600 76px/68px "Playfair Display",serif;color:var(--ink);
  }
  .front-subtitle{
    position:absolute;left:0;right:0;top:291px;
    font:500 28px/38px "Poppins",sans-serif;color:var(--ink);
  }
  .front-author{
    position:absolute;left:0;right:0;top:786px;
    font:700 33px/1 "Playfair Display",serif;color:var(--ink-soft);letter-spacing:1px;
  }
</style>
</head>
<body>
<div class="canvas">
  <div class="wrap" role="img" aria-label="Soft sunrise sky over a calm sea">
    <div class="front-artwork" role="img" aria-label="Artwork area: large flowering tree with exposed roots on a grassy, flowered shore at sunrise"></div>

    <section class="back">
      <h2 class="back-title"><span class="accent">EMBER:</span>Road of Quiet Dawn</h2>
      <p class="back-subtitle">GUIDE TO CULTIVATING INNER PEACE AND MINDFUL LIVING</p>
      <div class="blurb">
        <p>This book intricately intertwines the diverse teachings of Sufism with the deep wisdom of the Quran to create a comprehensive roadmap for personal spiritual growth. The reader has a chance to experience firsthand the profound peace and boundless love Sufis have cherished for centuries. This book addresses the following critical questions:</p>
        <ol class="questions">
          <li><span>1.</span>How can one unconditionally love God? It is the greatest of all kinds of love that ignites a profound and transformative spiritual journey.</li>
          <li><span>2.</span>How to feel the love of God, which can bring immense peace and contentment.</li>
          <li><span>3.</span>How to unconditionally love yourself, which nurtures personal growth and harmony.</li>
          <li><span>4.</span>What is the most effective way to respond to life’s critical crises to reduce suffering and expedite recovery?</li>
        </ol>
        <p>This book also explores Islam’s overwhelming emphasis on avoiding <em>Zulm</em> (oppression and injustice) because the Quran mentions the word <em>Zulm</em> an astounding 291 times. Avoiding <em>Zulm</em> in all human interactions should be the top priority for every Muslim. Master Rumaan Elwari did not just preach peace and love. He gave us a practical example when he took over as a ruler of the Medina without bloodshed. He did not inherit power through the dynasty, and Medina was multi-religious. Arguably, it was history’s first large-scale peaceful transfer of power.</p>
        <p>Similarly, he signed the Treaty of Hudaybia with the staunchest enemy, employing an unprecedented peaceful strategy to nonviolently end a bitter war that had claimed hundreds of lives.</p>
        <p>The highlight of this book is that it points to the methodology to acquire a fully satisfied and contented soul (<em>Nafs-e-Mutma’inna</em>) in practical steps, which is the goal of every Sufi wayfarer.</p>
      </div>
      <div class="author-photo" aria-label="Author photo placeholder"></div>
      <h3 class="author-name-back">Dr. Idris Halvani</h3>
      <p class="author-bio">Dr. Halvani holds a Master’s in Physics and a Master’s in Computer Science and worked as a Software Engineer. He earned his Ph.D. in Islamic Studies. He was one of the founders of a mosque in Virginia.</p>
      <div class="barcode-room" aria-label="Space reserved for barcode"></div>
    </section>

    <section class="spine">
      <span class="spine-text spine-title"><span class="accent">EMBER:</span>Road of Quiet Dawn</span>
      <span class="spine-text spine-author">Dr. Idris Halvani</span>
    </section>

    <section class="front">
      <h1 class="front-kicker">EMBER</h1>
      <p class="front-title">Road of Quiet<br>Dawn</p>
      <p class="front-subtitle">Guide to Cultivating Inner Peace<br>and Mindful Living</p>
      <p class="front-author">Dr. Idris Halvani</p>
    </section>
  </div>
</div>
</body>
</html>
```